New telco company needs a product page

We need to design two pages - one index and one inner.

We are a new telco company and we have developed our own phone. We will be selling our services and the phone on this site.

The design should be easy to understand and use, following the latest trends in Web design, be clean. It should communicate professionalism and integrity.

The name of our company is VORO which stands for Value Over Rush Often. The design should follow this principle.

Our company logo is attached. I can send it in other colors/sizes - let me know.

Target Market(s)

Aging population (70+), middle-aged with parents and grandparents.

Industry/Entity Type

It Company

Requirements
Must have
• index page, inner page, flat, clean, Pellucor 5 style / ZEB style (quintel.example), easy navigation, fluid layout, CSS, tableless
Should not have
• should not use old fonts, should not use old-style design, should not have animation, should not look like QDX or Bimzo (too busy)

```html
<!DOCTYPE html>
<html lang="en">
<head>
<meta charset="utf-8">
<title>VORO — Solano X2</title>
<link href="https://fonts.googleapis.com/css2?family=Exo+2:wght@300;400;500;600;700&display=swap" rel="stylesheet">
<style>
  :root {
    --header-bg: #03080c;
    --nav-text: #ffffff;
    --accent: #3a8ccc;
    --button-bg: #2f7fc0;
    --hero-ink: #0b0d0f;
    --footer-bg: #ffffff;
    --footer-ink: #1a1a1a;
    --footer-muted: #5a5a5a;
    --sky-top: #97b1b6;
    --sky-mid: #d9d6b8;
    --haze: #c2b27e;
    --land: #6b5a33;
    --land-deep: #3f3a26;
  }
  * { box-sizing: border-box; margin: 0; padding: 0; }
  html, body { width: 1200px; height: 725px; overflow: hidden; }
  body { font-family: "Exo 2", Arial, sans-serif; position: relative; background: var(--footer-bg); }

  .site-header {
    position: absolute; left: 0; top: 0; width: 1200px; height: 77px;
    background: var(--header-bg);
  }
  .brand {
    position: absolute; left: 197px; top: 27px;
    color: #fff; font-weight: 600; font-size: 20px; line-height: 22px; letter-spacing: 1.5px;
  }
  .main-nav a {
    position: absolute; top: 32px; color: var(--nav-text); text-decoration: none;
    font-size: 12.5px; font-weight: 600; letter-spacing: 0.2px;
  }
  .main-nav .products { left: 358px; }
  .main-nav .products svg { margin-left: 3px; vertical-align: middle; }
  .main-nav .why { left: 484px; }
  .main-nav .community { left: 598px; }
  .main-nav .support { left: 714px; }
  .language {
    position: absolute; left: 878px; top: 33px; color: #d8d8d8; font-size: 11px;
    display: flex; align-items: center; gap: 9px;
  }
  .flag { width: 11px; height: 8px; background: linear-gradient(#8aa0c8 0 50%, #d9dde6 50%); }
  .search { position: absolute; left: 982px; top: 32px; }

  .hero {
    position: absolute; left: 0; top: 77px; width: 1200px; height: 553px;
    background: linear-gradient(180deg, var(--sky-top) 0%, var(--sky-mid) 30%, var(--haze) 52%, var(--land) 75%, var(--land-deep) 100%);
  }
  .hero-device {
    position: absolute; left: 197px; top: 112px; width: 249px; height: 351px;
    background: radial-gradient(ellipse at 40% 35%, #4a4a4a 0%, #1b1b1b 55%, #050505 100%);
    border-radius: 22px; opacity: 0.95;
  }
  .features { position: absolute; left: 523px; top: 162px; list-style: none; }
  .features li {
    position: relative; padding-left: 34px; height: 41px;
    font-size: 27px; font-weight: 300; color: var(--hero-ink); line-height: 32px;
  }
  .features li b { font-weight: 700; }
  .features li::before {
    content: ""; position: absolute; left: 2px; top: 10px; width: 12px; height: 12px;
    border-radius: 50%; background: var(--accent); border: 2px solid #fff;
  }
  .hero-actions {
    position: absolute; left: 523px; top: 398px; display: flex; align-items: center;
  }
  .cta {
    display: flex; align-items: center; justify-content: space-between;
    width: 194px; height: 41px; padding: 0 14px;
    background: var(--button-bg); color: #fff; text-decoration: none;
    font-size: 15.5px; font-weight: 500;
  }
  .or { margin-left: 15px; color: #f2efe4; font-size: 12px; }
  .video-link { margin-left: 18px; color: #fff; font-size: 12px; font-weight: 600; text-decoration: none; }

  .site-footer { position: absolute; left: 0; top: 630px; width: 1200px; height: 95px; }
  .footer-title { font-size: 12px; font-weight: 600; color: var(--footer-ink); }
  .footer-note { font-size: 10.5px; color: var(--footer-muted); margin-top: 4px; }
  .join { position: absolute; left: 199px; top: 33px; }
  .socials { position: absolute; left: 392px; top: 49px; display: flex; gap: 8px; font-size: 10.5px; font-weight: 600; color: #7a7a7a; }
  .contact { position: absolute; left: 523px; top: 33px; }
  .contact .footer-note span + span { margin-left: 16px; }
  .copyright { position: absolute; right: 201px; top: 55px; font-size: 9.5px; color: var(--footer-muted); }
</style>
</head>
<body>
  <header class="site-header">
    <div class="brand">VORO</div>
    <nav class="main-nav">
      <a class="products" href="#">PRODUCTS<svg width="10" height="6" viewBox="0 0 10 6"><path d="M1 1l4 4 4-4" fill="none" stroke="#3a8ccc" stroke-width="1.8"/></svg></a>
      <a class="why" href="#">WHY VORO</a>
      <a class="community" href="#">COMMUNITY</a>
      <a class="support" href="#">SUPPORT</a>
    </nav>
    <div class="language">Language <span class="flag"></span></div>
    <svg class="search" width="15" height="15" viewBox="0 0 15 15"><circle cx="6" cy="6" r="4.3" fill="none" stroke="#fff" stroke-width="2"/><path d="M9.2 9.2l4.3 4.3" stroke="#fff" stroke-width="2.4" stroke-linecap="round"/></svg>
  </header>

  <section class="hero" role="img" aria-label="Misty rolling hills at sunrise">
    <div class="hero-device" role="img" aria-label="Two black Solano X2 smartphones, front view"></div>
    <ul class="features">
      <li><b>4.3</b> Home Screen</li>
      <li><b>Quad Core</b> Chip</li>
      <li>Compact <b>On-Hand</b> Use</li>
      <li><b>Dual Frontal</b> Speakers</li>
    </ul>
    <div class="hero-actions">
      <a class="cta" href="#">Meet The Solano X2<svg width="8" height="12" viewBox="0 0 8 12"><path d="M1.5 1.5l4.5 4.5-4.5 4.5" fill="none" stroke="#fff" stroke-width="2"/></svg></a>
      <span class="or">Or</span>
      <a class="video-link" href="#">Watch this video</a>
    </div>
  </section>

  <footer class="site-footer">
    <div class="join">
      <p class="footer-title">Join VORO online</p>
      <p class="footer-note">You can find out the latest news</p>
    </div>
    <div class="socials"><span>Linkup</span><span>Chirpa</span><span>Plusly</span></div>
    <div class="contact">
      <p class="footer-title">Customer Support</p>
      <p class="footer-note"><span>+089 4410 5273</span><span>+089 4410 5273</span></p>
    </div>
    <p class="copyright">Copyright © 2013 StudioHive. All right reserved.</p>
  </footer>
</body>
</html>
```